Poster Design to promote Adult Group Guitar Classes for Music School

We're a young music school trying to promote our Grown-Up Strum Starter Series classes, and need an eye catching poster design to promote the course. We'll be wanting to put the posters up on telegraph poles, community notice boards, shop front windows, cafes, shops and the around the general area of Sydney's Inner West, plus be able to covert it as a jpg image which we can forward to our mailing list and post on our website.

The poster should be visually appealing and incorporate images of what we are trying to promote.

We'd like the design to be professional, fun, creative and compliment our current logo design and colours.

Be sure to highlight 'Register Now'

Text to be used as follows:

STRUM STARTER SERIES CLASSES
For Beginner Adults

NEWTOWN

8 week Jam Packed Course
Small Groups (max. 6 people)
Guitars provided on site
Weekly hour long classes
Perfect introduction to learning the fundamentals
Materials Included
No music experience required

RESGISTER NOW – Limited Spaces
Visit our website for class times and start dates
www.brightreedmusic.com.au

T: (02) 7413 2958
E: info@brightreedmusic.com.au

PRIVATE MUSIC TUITION | ENSEMBLE | GROUP | GLEE CLUB

Industry/Entity Type

School

Requirements
Must have
• Bright Reed Music Logo

A3 poster size

Be in a print ready file for off-set printing. CMYK with 3mm bleed

```html
<!DOCTYPE html>
<html lang="en">
<head>
<meta charset="utf-8">
<title>Strum Starter Series Classes – Bright Reed Music</title>
<link href="https://fonts.googleapis.com/css2?family=Oswald:wght@400;500;600;700&display=swap" rel="stylesheet">
<style>
  :root {
    --bg: #000000;
    --red: #c81f2c;
    --yellow: #fff200;
    --guitar-deep: #3a1a08;
    --guitar-warm: #c9781c;
    --guitar-light: #e8a93a;
    --photo-dark: #141414;
    --photo-warm: #5a4632;
    --badge: #ffffff;
  }
  html, body {
    margin: 0;
    padding: 0;
    width: 1200px;
    height: 1119px;
    overflow: hidden;
    background: var(--bg);
  }
  .poster {
    position: relative;
    width: 1200px;
    height: 1119px;
    background: var(--bg);
    font-family: "Oswald", "Arial Narrow", sans-serif;
    overflow: hidden;
  }
  .centered {
    position: absolute;
    transform: translateX(-50%);
    text-align: center;
    white-space: nowrap;
    margin: 0;
  }
  .headline {
    left: 604px;
    top: -6px;
    color: var(--red);
    font-weight: 600;
    font-size: 76px;
    line-height: 1.1;
    letter-spacing: -0.5px;
  }
  .subhead {
    left: 604px;
    top: 72px;
    color: var(--red);
    font-weight: 500;
    font-size: 56px;
    line-height: 1.1;
  }
  .guitar-art {
    position: absolute;
    left: 0;
    top: 0;
    width: 235px;
    height: 1119px;
    background: linear-gradient(180deg, var(--guitar-deep) 0%, var(--guitar-warm) 55%, var(--guitar-light) 80%, var(--guitar-warm) 100%);
    opacity: 0.85;
  }
  .players-photo {
    position: absolute;
    left: 82px;
    top: 146px;
    width: 690px;
    height: 542px;
    background: radial-gradient(ellipse at 50% 45%, var(--photo-warm) 0%, var(--photo-dark) 70%);
  }
  .location {
    left: 1006px;
    top: 186px;
    color: var(--yellow);
    font-weight: 600;
    font-size: 40px;
    line-height: 1.2;
    letter-spacing: 2px;
  }
  .contact {
    position: absolute;
    left: 1006px;
    color: var(--yellow);
    font-weight: 500;
    font-size: 25px;
    line-height: 34px;
  }
  .contact.visit { top: 265px; }
  .contact.phone { top: 401px; }
  .contact.services { top: 503px; }
  .features {
    position: absolute;
    top: 702px;
    color: var(--yellow);
    font-weight: 500;
    font-size: 42px;
    line-height: 54.5px;
  }
  .features.left { left: 356px; }
  .features.right { left: 901px; }
  .register {
    left: 609px;
    top: 970px;
    color: var(--yellow);
    font-weight: 600;
    font-size: 44px;
    line-height: 1.3;
  }
  .brand {
    position: absolute;
    left: 445px;
    top: 1046px;
    display: flex;
    align-items: center;
    gap: 14px;
  }
  .brand-name {
    color: var(--yellow);
    font-weight: 500;
    font-size: 34px;
    line-height: 1;
    white-space: nowrap;
  }
  .brand-mark {
    width: 72px;
    height: 72px;
    background: var(--badge);
  }
</style>
</head>
<body>
  <main class="poster">
    <div class="guitar-art" role="img" aria-label="Photo of a classical guitar standing upright along the left edge"></div>

    <h1 class="centered headline">STRUM STARTER SERIES CLASSES</h1>
    <h2 class="centered subhead">For Beginner Adults</h2>

    <div class="players-photo" role="img" aria-label="Photo of a guitarist in black seated on a stool, shown twice playing a classical guitar"></div>

    <p class="centered location">NEWTOWN</p>
    <p class="centered contact visit">Visit our website for class times<br>and start dates<br>www.brightreedmusic.com.au</p>
    <p class="centered contact phone">T: (02) 7413 2958<br>E: info@brightreedmusic.com.au</p>
    <p class="centered contact services">PRIVATE MUSIC TUITION | ENSEMBLE<br>| GROUP | GLEE CLUB</p>

    <p class="centered features left">8 week Jam Packed Course<br>Small Groups (max. 6 people)<br>Guitars provided on site<br>Weekly hour long classes</p>
    <p class="centered features right">Perfect introduction to learning<br>the fundamentals<br>Materials Included<br>No music experience required</p>

    <p class="centered register">RESGISTER NOW – Limited Spaces</p>

    <div class="brand">
      <span class="brand-name">Bright Reed Music</span>
      <span class="brand-mark"></span>
    </div>
  </main>
</body>
</html>
```